Business card with logo and words.

Colours: aqua and white (but open to suggestions).
Double sided card ok.
Need to convey competence, calmness, listening skills
Words:
Quiet Harbour Care Guidance
Ruth Pemberly
RN, RM, MQDNS, Grad Dip Gr & Pall Care Couns, Grad Cert Pall Care in Aged Care
quietharbourcg@mailvane.net

```html
<!DOCTYPE html>
<html lang="en">
<head>
<meta charset="utf-8">
<title>Quiet Harbour Care Guidance – Business Card</title>
<link rel="stylesheet" href="https://fonts.googleapis.com/css2?family=Raleway:wght@400;500;600&family=Tinos:ital@1&display=swap">
<style>
  :root {
    --page: #f4f4f4;
    --label: #333333;
    --card-aqua: #14bff0;
    --card-white: #ffffff;
    --ink: #1a1a1a;
    --curl: #0a6f8c;
    --title-shadow: rgba(0, 60, 90, 0.35);
  }
  * { margin: 0; padding: 0; box-sizing: border-box; }
  html, body { width: 1200px; height: 1021px; overflow: hidden; }
  body { background: var(--page); position: relative; font-family: "Raleway", sans-serif; }

  .side-label {
    position: absolute; left: 0; width: 1200px; text-align: center;
    font: 400 20px "Raleway", sans-serif; color: var(--label);
  }
  .side-label--front { top: 36px; }
  .side-label--back { top: 515px; }

  .card {
    position: absolute; left: 278px; width: 639px; height: 383px;
    background: var(--card-aqua); overflow: hidden;
    box-shadow: 0 10px 14px -8px rgba(0, 0, 0, 0.25);
  }
  .card--front { top: 74px; }
  .card--back { top: 553px; }

  .brand {
    position: absolute; left: 28px; top: 42px;
    display: flex; align-items: center; gap: 12px;
  }
  .brand__mark { width: 20px; height: 20px; border-radius: 50%; background: var(--card-white); }
  .brand__name { font: 600 26px "Raleway", sans-serif; color: var(--card-white); letter-spacing: 0.5px; }

  .title-line {
    position: absolute; font: italic 400 55px/1 "Tinos", serif; color: var(--card-white);
    text-shadow: 1px 2px 3px var(--title-shadow); white-space: nowrap;
  }
  .title-line--one { left: 197px; top: 164px; }
  .title-line--two { right: 24px; top: 239px; }
  .rule { position: absolute; height: 1.5px; background: var(--card-white); }
  .rule--one { left: 74px; top: 226px; width: 262px; }
  .rule--two { left: 270px; top: 299px; width: 339px; }

  .person-name {
    position: absolute; right: 40px; top: 172px;
    font: italic 400 52px "Tinos", serif; color: var(--card-white);
    text-shadow: 1px 2px 3px var(--title-shadow); white-space: nowrap;
  }
  .credentials {
    position: absolute; right: 40px; top: 244px; text-align: right;
    font: 500 13px/18px "Raleway", sans-serif; color: var(--ink);
  }

  .email {
    position: absolute; right: 40px; bottom: 17px;
    font: 400 19px "Raleway", sans-serif; color: var(--card-white);
  }
  .curl { position: absolute; right: 0; bottom: 0; width: 22px; height: 22px; }
</style>
</head>
<body>
  <div class="side-label side-label--front">Front</div>
  <section class="card card--front">
    <div class="brand">
      <span class="brand__mark"></span>
      <span class="brand__name">Quiet Harbour</span>
    </div>
    <div class="title-line title-line--one">Care</div>
    <div class="rule rule--one"></div>
    <div class="title-line title-line--two">Guidance</div>
    <div class="rule rule--two"></div>
    <div class="email">quietharbourcg@mailvane.net</div>
    <svg class="curl" viewBox="0 0 22 22"><polygon points="22,0 22,22 0,22" fill="var(--page)"/><polygon points="22,0 0,22 0,0" fill="var(--curl)"/></svg>
  </section>

  <div class="side-label side-label--back">Back</div>
  <section class="card card--back">
    <div class="brand">
      <span class="brand__mark"></span>
      <span class="brand__name">Quiet Harbour</span>
    </div>
    <div class="person-name">Ruth Pemberly</div>
    <div class="credentials">
      <div>RN, RM, MQDNS</div>
      <div>Grad Dip Gr &amp; Pall Care Couns</div>
      <div>Grad Cert Pall Care in Aged Care</div>
    </div>
    <div class="email">quietharbourcg@mailvane.net</div>
    <svg class="curl" viewBox="0 0 22 22"><polygon points="22,0 22,22 0,22" fill="var(--page)"/><polygon points="22,0 0,22 0,0" fill="var(--curl)"/></svg>
  </section>
</body>
</html>
```